Trailbound Hub Outfitter Directory

Hero Section
Image: A serene and picturesque camping landscape with a lake, mountains, and a few trees There is a circle of people sitting around a campfire. The image should be high-quality and visually appealing.
Headline: "Introducing Trailboundhub.com's Outfitter Directory"
Subheading: "Join our directory of trusted outfitters and reach a targeted audience of camping enthusiasts."
Call-to-Action (CTA) Button: "Learn More" or "Join Now"
Color scheme: Match trailboundhub.com and the logo
Example:
[Image: A serene and picturesque camping landscape with a lake, mountains, and a few trees]
Introducing Trailboundhub.com's Outfitter Directory
Join our directory of trusted outfitters and reach a targeted audience of camping enthusiasts.
Learn More
Benefits Section
Image: A group of happy campers sitting around a campfire, roasting marshmallows and telling stories.
Headline: "Benefits of Joining Our Directory"
Bullet points:
"Increase your exposure and visibility to potential customers"
"Book more trips and generate more revenue"
"Access a targeted audience of camping enthusiasts"
Color scheme: match trailboundhub.com
Example:
[Image: A group of happy campers sitting around a campfire, roasting marshmallows and telling stories]
Benefits of Joining Our Directory
• Increase your exposure and visibility to potential customers • Book more trips and generate more revenue • Access a targeted audience of camping enthusiasts
Features Section
Image: A screenshot of the directory's search functionality, showing a list of outfitters with their logos, names, and locations.
Headline: "Features of Our Outfitter Directory"
Bullet points:
"Search functionality to find outfitters by location, activity, or type"
"Outfitter profiles with detailed information and reviews"
"Booking system to make it easy for customers to book trips"
Example:
[Image: A screenshot of the directory's search functionality, showing a list of outfitters with their logos, names, and locations]
Features of Our Outfitter Directory
• Search functionality to find outfitters by location, activity, or type • Outfitter profiles with detailed information and reviews • Booking system to make it easy for customers to book trips
CTA Section
Image: A simple and clean design with a prominent call-to-action button.
Headline: "Express Interest in Joining Our Directory"
Call-to-Action (CTA) Button: "Express Interest" or "Join Now"

Example:
[Image: A simple and clean design with a prominent call-to-action button]
Express Interest in Joining Our Directory
Express Interest
Contact Information Section
Image: A simple and clean design with a form to collect contact information.
Headline: "Get in Touch with Us"
Form fields:
Name
Email
Phone
Website

```html
<!DOCTYPE html>
<html lang="en">
<head>
<meta charset="utf-8">
<title>Trailbound Hub Outfitter Directory</title>
<link href="https://fonts.googleapis.com/css2?family=Oswald:wght@500;600;700&family=Inter:wght@400;500;600;700&display=swap" rel="stylesheet">
<style>
:root{
  --teal:#00a0a6;
  --frame:#0b7b7d;
  --navy:#0f2747;
  --orange:#f26522;
  --mint:#e6f4f4;
  --footer:#05454b;
  --footer-dark:#033a3f;
  --ink:#1f2a37;
  --muted:#555f6b;
  --white:#fff;
}
*{box-sizing:border-box;margin:0;padding:0}
html,body{width:1200px;height:3463px;overflow:hidden}
body{background:var(--frame);font-family:'Inter',sans-serif;color:var(--ink);position:relative}
.page{position:absolute;left:50px;top:73px;width:1100px}
.abs{position:absolute}
.display{font-family:'Oswald',sans-serif;font-weight:600;text-transform:uppercase;color:var(--navy);letter-spacing:.2px}
.btn{position:absolute;display:flex;align-items:center;justify-content:center;border-radius:4px;font-size:13px;font-weight:500}
.btn-teal{background:var(--teal);color:var(--white)}
.btn-outline{background:var(--white);color:var(--orange);border:2px solid var(--orange)}

/* hero */
.hero{position:relative;height:689px;background:linear-gradient(100deg,#1b2520 0%,#2c3227 35%,#4a3a2a 60%,#2d2a22 100%);overflow:hidden}
.hero-photo{position:absolute;inset:0;background:radial-gradient(circle at 29% 84%,rgba(240,150,50,.55),transparent 22%),radial-gradient(circle at 75% 45%,rgba(150,110,80,.4),transparent 35%)}
.brand{position:absolute;left:84px;top:12px;display:flex;align-items:center;gap:8px;color:var(--white);font-size:15px;font-weight:600}
.brand-dot{width:40px;height:40px;border-radius:50%;background:var(--white)}
.nav{position:absolute;top:31px;left:0;font-size:13px;color:var(--white)}
.nav a{position:absolute;white-space:nowrap;color:var(--white);text-decoration:none}
.nav .active{color:#5fd3d6;font-weight:600}
.hero-title{position:absolute;left:91px;top:186px;font-size:53px;line-height:56px;color:var(--white);font-family:'Oswald',sans-serif;font-weight:700;text-transform:uppercase}
.hero-sub{position:absolute;left:91px;top:370px;width:460px;font-size:18px;line-height:28px;color:#f0f0f0}

/* benefits */
.benefits{position:relative;height:518px;background:var(--white)}
.benefits h2{position:absolute;top:66px;width:100%;text-align:center;font-size:40px}
.benefit{position:absolute;top:144px;width:268px;text-align:center;font-size:14.5px;line-height:21px;color:var(--ink)}
.benefit .ph{height:228px;margin-bottom:14px}

/* features */
.features{position:relative;height:950px;background:var(--mint)}
.features h2{position:absolute;left:91px;top:64px;font-size:40px}
.feature-row{position:absolute;left:91px;top:145px;width:918px;height:252px;background:var(--white)}
.search-shot{position:absolute;left:0;top:0;width:382px;height:252px;background:linear-gradient(135deg,#6e8a3c,#a9b86a 45%,#566c2e)}
.search-shot .inner{position:absolute;left:35px;top:32px;width:246px;height:108px;background:linear-gradient(160deg,#8fb2d6,#9aae70)}
.search-bar{position:absolute;left:48px;top:135px;width:300px;height:36px;border-radius:18px;background:var(--white);font-size:14px;color:#888;padding:9px 12px}
.search-bar .go{position:absolute;right:-2px;top:-1px;width:38px;height:38px;border-radius:50%;background:var(--orange)}
.chip{position:absolute;top:190px;height:30px;border-radius:15px;font-size:10px;padding:8px 10px;color:var(--navy);border:2px solid var(--white)}
.feature-copy{position:absolute;left:410px;top:60px;width:470px}
.feature-copy h3{font-size:19px;margin-bottom:8px}
.feature-copy p{font-size:13.5px;line-height:21px;color:var(--muted)}
.card{position:absolute;top:420px;width:448px;height:461px;background:var(--white)}
.mock{position:absolute;left:23px;top:34px;border:1px solid #ddd;border-radius:8px;background:var(--white);box-shadow:0 4px 10px rgba(0,0,0,.06)}
.card h3{position:absolute;left:23px;top:318px;font-size:19px}
.card p{position:absolute;left:23px;top:354px;width:330px;font-size:13.5px;line-height:21px;color:var(--muted)}
.thumb{position:absolute;width:66px;height:47px}
.mock-label{position:absolute;font-size:12px;font-weight:600;color:var(--ink)}

/* cta */
.cta{position:relative;height:302px;background:var(--teal);text-align:center;color:var(--white)}
.cta h2{position:absolute;top:54px;width:100%;font-size:40px;color:var(--white)}
.cta p{position:absolute;top:124px;width:100%;font-size:19.5px;line-height:24px}

/* contact */
.contact{position:relative;height:524px;background:var(--white)}
.contact h2{position:absolute;top:68px;width:100%;text-align:center;font-size:40px}
.field{position:absolute;border:1px solid #9aa3ad;font-size:14px;padding:13px 18px;color:var(--ink)}
.submit{position:absolute;left:240px;top:387px;width:647px;height:49px;background:var(--teal);color:var(--white);font-weight:600;font-size:15px;display:flex;align-items:center;justify-content:center}

/* footer */
.footer{position:relative;height:287px;background:var(--footer);color:var(--white)}
.footer h4{font-family:'Oswald',sans-serif;font-weight:600;font-size:14px;text-transform:uppercase;position:absolute;top:56px}
.footer .links{position:absolute;top:88px;font-size:12px;line-height:28px}
.footer-brand{position:absolute;left:95px;top:67px;display:flex;align-items:center;gap:8px;font-size:15px;font-weight:600}
.footer-brand span{width:40px;height:40px;border-radius:50%;background:var(--white)}
.footer-about{position:absolute;left:91px;top:140px;width:270px;font-size:12px;line-height:14px}
.follow{position:absolute;left:91px;top:197px;font-family:'Oswald',sans-serif;font-size:11px;font-weight:600}
.social{position:absolute;top:232px;width:18px;height:18px;border-radius:50%;background:var(--white)}
.news-input{position:absolute;left:801px;top:161px;width:208px;height:33px;background:var(--white);color:var(--ink);font-size:12px;display:flex;align-items:center;justify-content:center}
.news-btn{position:absolute;left:801px;top:201px;width:208px;height:32px;background:var(--teal);font-size:12px;font-weight:600;display:flex;align-items:center;justify-content:center}
.copyright{height:47px;background:var(--footer-dark);color:var(--white);font-size:12px;font-weight:600;display:flex;align-items:center;justify-content:center}
</style>
</head>
<body>
<div class="page">

  <section class="hero">
    <div class="hero-photo" role="img" aria-label="Friends playing guitar beside a campfire in a forest at dusk, with a tent and a dog nearby"></div>
    <div class="brand"><span class="brand-dot"></span>Trailbound Hub</div>
    <nav class="nav">
      <a class="active" style="left:376px">• Home</a>
      <a style="left:457px">Campgrounds</a>
      <a style="left:572px">Activities</a>
      <a style="left:661px">Pricing</a>
    </nav>
    <div class="btn btn-teal" style="left:779px;top:24px;width:102px;height:32px">Join Now</div>
    <div class="btn btn-outline" style="left:895px;top:24px;width:102px;height:32px">Learn More</div>
    <h1 class="hero-title">Introducing<br>Trailboundhub.com's<br>Outfitter Directory</h1>
    <p class="hero-sub">Join our directory of trusted outfitters and reach a targeted audience of camping enthusiasts.</p>
    <div class="btn btn-teal" style="left:91px;top:446px;width:122px;height:41px">Join Now</div>
    <div class="btn btn-outline" style="left:230px;top:446px;width:120px;height:41px">Learn More</div>
  </section>

  <section class="benefits">
    <h2 class="display">Benefits of Joining Our Directory</h2>
    <div class="benefit" style="left:91px"><div class="ph" role="img" aria-label="Group of friends roasting marshmallows around a campfire" style="background:linear-gradient(135deg,#3b3a2c,#7a5232 55%,#2a2a22)"></div>Increase your exposure and visibility to potential customers</div>
    <div class="benefit" style="left:416px"><div class="ph" role="img" aria-label="Excited woman holding a fan of banknotes on a yellow background" style="background:linear-gradient(135deg,#ffc20e,#f7b500)"></div>Book more trips and generate<br>more revenue</div>
    <div class="benefit" style="left:741px"><div class="ph" role="img" aria-label="Family at a campsite picnic table with camping chairs" style="background:linear-gradient(180deg,#7d9a62,#6a7a4e 50%,#7b6a52)"></div>Access a targeted audience<br>of camping enthusiasts</div>
  </section>

  <section class="features">
    <h2 class="display">Features of Our Outfitter Directory</h2>
    <div class="feature-row">
      <div class="search-shot" role="img" aria-label="Blurred family camping scene behind a directory search interface">
        <div class="inner"></div>
        <div class="search-bar">Search<span class="go"></span></div>
        <div class="chip" style="left:56px;width:80px;background:#bfe6e6">Activity ⌄</div>
        <div class="chip" style="left:145px;width:88px;background:#f6b8a0">Location ⌄</div>
        <div class="chip" style="left:241px;width:94px;background:#8fd36a">Type ⌄</div>
      </div>
      <div class="feature-copy">
        <h3 class="display">Features of Our Outfitter Directory</h3>
        <p>Our directory features a powerful search function that enables users to find outfitters based on criteria such as location, activity type (e.g., hiking, fishing, kayaking), and specific services (e.g., guided tours, equipment rentals).</p>
      </div>
    </div>

    <div class="card" style="left:91px">
      <div class="mock" style="width:338px;height:245px">
        <div class="abs" role="img" aria-label="Outfitter team group photo" style="left:14px;top:38px;width:78px;height:78px;border-radius:50%;background:linear-gradient(135deg,#a36b4a,#6b4a3a)"></div>
        <div class="abs" style="left:114px;top:22px;font-size:8px;color:var(--muted)"><span style="display:inline-block;width:36px;height:10px;border-radius:5px;background:#c9a080;vertical-align:middle"></span> 14+ Members</div>
        <div class="abs" style="left:114px;top:44px;font-size:15px;font-weight:700;color:var(--navy)">Ridgeline Trails Outfitters</div>
        <div class="abs" style="left:114px;top:68px;width:210px;font-size:10px;line-height:14px;color:var(--muted)">Ridgeline Trails Outfitters specializes in guided hiking and camping experiences...</div>
        <div class="abs" style="left:114px;top:112px;font-size:15px;color:#f5b400;letter-spacing:3px">★★★★<span style="color:#ccc">★</span> <span style="font-size:9px;color:var(--ink);letter-spacing:0">4.5/5.0</span></div>
        <div class="mock-label" style="left:14px;top:152px">Service Offered</div>
        <div class="thumb" role="img" aria-label="Hiker" style="left:14px;top:176px;background:#a6bcd2"></div>
        <div class="thumb" role="img" aria-label="Tent" style="left:94px;top:176px;background:#e0b23a"></div>
        <div class="thumb" role="img" aria-label="Lion" style="left:173px;top:176px;background:#c9994d"></div>
      </div>
      <h3 class="display">Detailed Outfitter Profiles</h3>
      <p>Each outfitter in our directory has a dedicated profile page that provides in-depth information.</p>
    </div>

    <div class="card" style="left:561px">
      <div class="mock" style="width:338px;height:245px">
        <div class="mock-label" style="left:14px;top:24px">Service Offered</div>
        <div class="thumb" style="left:14px;top:48px;background:#a6bcd2"></div>
        <div class="thumb" style="left:94px;top:48px;background:#e0b23a"></div>
        <div class="thumb" style="left:173px;top:48px;background:#3f4a36"></div>
        <div class="thumb" style="left:253px;top:48px;background:#5b5a52"></div>
        <div class="thumb" style="left:14px;top:108px;background:#b5562a"></div>
        <div class="thumb" style="left:94px;top:108px;background:#9bb07a"></div>
        <div class="thumb" style="left:173px;top:108px;background:#9a5a2e"></div>
        <div class="thumb" style="left:253px;top:108px;background:#c35a4a"></div>
        <div class="thumb" style="left:14px;top:168px;background:#c2a37a"></div>
        <div class="thumb" style="left:94px;top:168px;background:#2e2418"></div>
        <div class="thumb" style="left:173px;top:168px;background:#c9994d"></div>
        <div class="thumb" style="left:253px;top:168px;background:#4a3a32"></div>
      </div>
      <h3 class="display">Booking System</h3>
      <p style="width:320px">Booking system to make it easy for customers to book trips</p>
      <div class="btn btn-teal" style="left:26px;top:399px;width:122px;height:42px">Book Now</div>
    </div>
  </section>

  <section class="cta">
    <h2 class="display">Interest in Joining Our Directory</h2>
    <p>The Online collaborative whiteboard platform to bring<br>team together , anytime, any where</p>
    <div class="btn" style="left:489px;top:192px;width:122px;height:42px;background:var(--white);color:var(--teal)">Join Now</div>
  </section>

  <section class="contact">
    <h2 class="display">Get in Touch With Us</h2>
    <div class="field" style="left:240px;top:163px;width:318px;height:45px">Name</div>
    <div class="field" style="left:570px;top:163px;width:317px;height:45px">Email Id</div>
    <div class="field" style="left:240px;top:221px;width:318px;height:45px">Phone</div>
    <div class="field" style="left:570px;top:221px;width:317px;height:45px">Website</div>
    <div class="field" style="left:240px;top:278px;width:647px;height:98px">Message</div>
    <div class="submit">Submit Now</div>
  </section>

  <footer>
    <div class="footer">
      <div class="footer-brand"><span></span>Trailbound Hub</div>
      <p class="footer-about">Your go-to for outdoor tips, gear reviews, and adventures. Making nature your second home. Join the journey!</p>
      <div class="follow">FOLLOW US</div>
      <span class="social" style="left:91px"></span>
      <span class="social" style="left:123px"></span>
      <span class="social" style="left:154px"></span>

      <h4 style="left:407px">Popular Collections</h4>
      <div class="links" style="left:407px">Backpacks<br>Stoves<br>Camp Kitchen<br>Health &amp; Safety</div>
      <h4 style="left:614px">Customer Service</h4>
      <div class="links" style="left:614px">Refund Policy<br>Privacy Policy<br>Terms of Service</div>
      <h4 style="left:798px">Keep in Touch</h4>
      <p class="abs" style="left:798px;top:95px;width:210px;font-size:12px;line-height:14px">Subscribe to our newsletter to receive updates on new products and exclusive subscriber-only offers.</p>
      <div class="news-input">Enter Email Id</div>
      <div class="news-btn">SUBMIT NOW</div>
    </div>
    <div class="copyright">COPYRIGHT © 2012 - 2024 TRAILBOUND HUB ®. ALL RIGHTS RESERVED.</div>
  </footer>

</div>
</body>
</html>
```